Financial Service Company Need Business Card Design

This is a new startup company, first of its kind to offer this service. We facilitate the movement of deposit funds electronically between home buyers and real estate brokerages.Our customers are DOMIVANS®, real estate brokerages, and home buyers, we identify ourselves as a financial/technology company.
Not looking for anything too flashy. Just a clean design that shows the logo, contact info, etc. Company colors can be seen on attached logo, and 'coming soon page'
www.quorvanta.ca

```html
<!DOCTYPE html>
<html lang="en">
<head>
<meta charset="utf-8">
<title>Quorvanta – Business Card</title>
<link rel="stylesheet" href="https://fonts.googleapis.com/css2?family=Exo+2:wght@400;500;600;700&display=swap">
<style>
  :root {
    --brand-orange: #f0603a;
    --brand-grey: #66676b;
    --card-white: #ffffff;
    --card-shade: #ececec;
    --page-bg: #e9e7e3;
    --text-light: #ffffff;
  }
  * { margin: 0; padding: 0; box-sizing: border-box; }
  html, body {
    width: 1200px;
    height: 828px;
    overflow: hidden;
    background: var(--page-bg);
    font-family: "Exo 2", sans-serif;
  }
  .canvas {
    position: relative;
    width: 1200px;
    height: 828px;
    display: flex;
    align-items: center;
    justify-content: center;
    gap: 40px;
  }
  .card {
    width: 540px;
    height: 309px;
    box-shadow: 0 6px 18px rgba(0,0,0,0.18);
    display: block;
  }
  .wordmark {
    font-family: "Exo 2", sans-serif;
    font-weight: 700;
    fill: var(--brand-grey);
  }
  .wordmark-large { fill: var(--brand-orange); }
  .website-front {
    font-family: "Exo 2", sans-serif;
    font-size: 15px;
    letter-spacing: 4px;
    fill: var(--text-light);
  }
  .person-name {
    font-family: "Exo 2", sans-serif;
    font-weight: 500;
    font-size: 19px;
    letter-spacing: 0.5px;
    fill: var(--text-light);
  }
  .person-title, .contact-line {
    font-family: "Exo 2", sans-serif;
    font-size: 11.5px;
    fill: var(--text-light);
  }
  .contact-icon { fill: var(--text-light); }
  .contact-icon-line { fill: none; stroke: var(--text-light); stroke-width: 1.2; }
</style>
</head>
<body>
<main class="canvas">

  <!-- Front of card -->
  <svg class="card card-front" viewBox="0 0 540 309" xmlns="http://www.w3.org/2000/svg" aria-label="Business card front">
    <defs>
      <linearGradient id="front-white" x1="0" y1="0" x2="0" y2="1">
        <stop offset="0" stop-color="var(--card-white)"/>
        <stop offset="1" stop-color="var(--card-shade)"/>
      </linearGradient>
    </defs>
    <rect class="card-base" width="540" height="309" fill="url(#front-white)"/>
    <path class="grey-band" d="M0 238 Q 400 218 540 28 L540 309 L0 309 Z" fill="var(--brand-grey)"/>
    <path class="orange-curve" d="M0 235 Q 400 215 540 25" fill="none" stroke="var(--brand-orange)" stroke-width="6"/>
    <g class="brand-lockup">
      <rect x="148" y="106" width="24" height="24" fill="var(--brand-orange)"/>
      <text class="wordmark" x="182" y="129" font-size="30">Quorvanta</text>
    </g>
    <text class="website-front" x="345" y="275" text-anchor="middle">www.quorvanta.ca</text>
  </svg>

  <!-- Back of card -->
  <svg class="card card-back" viewBox="0 0 540 309" xmlns="http://www.w3.org/2000/svg" aria-label="Business card back">
    <defs>
      <linearGradient id="back-white" x1="0" y1="0" x2="1" y2="1">
        <stop offset="0" stop-color="var(--card-shade)"/>
        <stop offset="0.5" stop-color="var(--card-white)"/>
        <stop offset="1" stop-color="var(--card-shade)"/>
      </linearGradient>
    </defs>
    <rect class="card-base" width="540" height="309" fill="var(--brand-grey)"/>
    <path class="white-field" d="M0 150 Q 250 90 390 309 L0 309 Z" fill="url(#back-white)"/>
    <path class="orange-curve" d="M0 147 Q 252 86 394 309" fill="none" stroke="var(--brand-orange)" stroke-width="6"/>

    <text class="wordmark wordmark-large" x="150" y="238" font-size="38" text-anchor="middle">Quorvanta</text>

    <g class="contact-block" text-anchor="end">
      <text class="person-name" x="515" y="42">MARTIN OKAFOR</text>
      <text class="person-title" x="515" y="60">Managing Director</text>

      <text class="contact-line" x="515" y="100">217 9th floor Plaza</text>
      <text class="contact-line" x="515" y="116">Harbour Street TRN</text>

      <text class="contact-line" x="497" y="152">014 555 0192</text>
      <text class="contact-line" x="497" y="170">014 555 0192</text>
      <text class="contact-line" x="497" y="188">014 555 0192</text>
      <text class="contact-line" x="497" y="206">martin@quorvanta.ca</text>
      <text class="contact-line" x="497" y="224">www.quorvanta.ca</text>
    </g>

    <g class="contact-icons">
      <!-- phone -->
      <path class="contact-icon" d="M504 143 q2 -1 3 1 l1 2 q0 1 -1 2 q1 2 3 3 q1 -1 2 -1 l2 1 q2 1 1 3 q-1 2 -3 1 q-5 -2 -8 -8 q-1 -2 0 -4 z"/>
      <!-- mobile -->
      <rect class="contact-icon-line" x="506" y="160" width="7" height="11" rx="1"/>
      <!-- fax -->
      <rect class="contact-icon" x="504" y="181" width="11" height="7" rx="1"/>
      <rect class="contact-icon" x="506" y="178" width="7" height="3"/>
      <!-- email -->
      <rect class="contact-icon-line" x="504" y="198" width="11" height="8"/>
      <path class="contact-icon-line" d="M504 198 l5.5 4.5 l5.5 -4.5"/>
      <!-- globe -->
      <circle class="contact-icon-line" cx="509.5" cy="220" r="5"/>
      <path class="contact-icon-line" d="M504.5 220 h10 M509.5 215 q-3 5 0 10 q3 -5 0 -10"/>
    </g>
  </svg>

</main>
</body>
</html>
```